Ridgecrest Ag, LLC
Business cards, letterhead, envelopes
Project: Ridgecrest Ag, LLC
Ridgecrest Ag, LLC - Consulting
Creative Brief
Professional
Warren Colbeck
P.O. Box 517 Alder Springs, CA 93940
warren@ridgecrestag-example.com
1. I want to use my logo and will upload it. 2. I like clean, uncluttered design. 3. OK to think a little out of the box. 4. May be OK to use a different font than logo. 5. May be OK to use tagline "same dirt - new rules" differently (i.e., not right under Ridgecrest Ag as shown in logo).

```html
<!DOCTYPE html>
<html lang="en">
<head>
<meta charset="utf-8">
<title>Ridgecrest Ag — Business Card</title>
<link rel="stylesheet" href="https://fonts.googleapis.com/css2?family=PT+Sans:wght@400;700&display=swap">
<style>
  :root {
    --maroon: #5a0f15;
    --gold: #f4b233;
    --paper: #ffffff;
    --backdrop: #ece8e2;
    --white: #ffffff;
  }
  html, body {
    margin: 0;
    width: 1200px;
    height: 965px;
    overflow: hidden;
    background: var(--backdrop);
    font-family: "PT Sans", sans-serif;
  }
  .card {
    position: absolute;
    left: 80px;
    top: 187px;
    width: 1040px;
    height: 590px;
    border-radius: 28px;
    overflow: hidden;
    background: var(--paper);
  }
  .card-swoosh {
    position: absolute;
    inset: 0;
  }
  .brand {
    position: absolute;
    left: 0;
    width: 884px;
    top: 140px;
    text-align: center;
    color: var(--maroon);
  }
  .brand-name {
    margin: 0;
    font-size: 62px;
    font-weight: 700;
    letter-spacing: 1px;
    line-height: 1;
  }
  .brand-tagline {
    margin: 14px 0 0;
    font-size: 24px;
    font-weight: 400;
    font-style: normal;
    letter-spacing: 1px;
    line-height: 1;
  }
  .holder-name {
    position: absolute;
    left: 126px;
    top: 498px;
    margin: 0;
    font-size: 44px;
    font-weight: 700;
    line-height: 1.1;
    color: var(--gold);
  }
  .address {
    position: absolute;
    right: 46px;
    top: 300px;
    margin: 0;
    font-style: normal;
    font-size: 27px;
    line-height: 34px;
    text-align: right;
    color: var(--white);
  }
  .contact-list {
    position: absolute;
    right: 36px;
    top: 392px;
    margin: 0;
    padding: 0;
    list-style: none;
    color: var(--white);
    font-size: 27px;
  }
  .contact-item {
    display: flex;
    justify-content: flex-end;
    align-items: center;
    height: 43px;
    gap: 16px;
  }
  .contact-icon {
    width: 26px;
    height: 26px;
    flex: none;
  }
</style>
</head>
<body>
  <section class="card">
    <svg class="card-swoosh" viewBox="0 0 1040 590" width="1040" height="590" aria-hidden="true">
      <path d="M0,428 C 330,440 720,330 1040,160 L1040,590 L0,590 Z" fill="var(--maroon)"/>
      <path d="M150,430 C 520,420 790,320 920,178 C 800,330 540,440 150,430 Z" fill="var(--gold)"/>
    </svg>

    <header class="brand">
      <h1 class="brand-name">Ridgecrest Ag</h1>
      <p class="brand-tagline">Rooted Advice • Fresh Thinking</p>
    </header>

    <h2 class="holder-name">Warren Colbeck</h2>

    <address class="address">
      P.O. Box 517<br>
      Alder Springs, CA 93940
    </address>

    <ul class="contact-list">
      <li class="contact-item">
        <span>(209) 555-0148</span>
        <svg class="contact-icon" viewBox="0 0 24 24" aria-label="mobile">
          <rect x="7" y="3" width="10" height="18" rx="2" fill="none" stroke="var(--white)" stroke-width="2"/>
          <rect x="9" y="6" width="6" height="6" fill="var(--white)"/>
        </svg>
      </li>
      <li class="contact-item">
        <span>(209) 555-0172</span>
        <svg class="contact-icon" viewBox="0 0 24 24" aria-label="fax">
          <rect x="7" y="3" width="10" height="7" fill="none" stroke="var(--white)" stroke-width="2"/>
          <rect x="4" y="10" width="16" height="10" rx="1.5" fill="var(--white)"/>
          <rect x="8" y="16" width="8" height="2" fill="var(--maroon)"/>
        </svg>
      </li>
      <li class="contact-item">
        <span>warren@ridgecrestag-example.com</span>
        <svg class="contact-icon" viewBox="0 0 24 24" aria-label="email">
          <circle cx="12" cy="12" r="3.5" fill="none" stroke="var(--white)" stroke-width="2.2"/>
          <path d="M15.5,9 V13.5 C15.5,16 19.5,16 19.5,12 A7.5,7.5 0 1 0 16,18.5" fill="none" stroke="var(--white)" stroke-width="2.2"/>
        </svg>
      </li>
      <li class="contact-item">
        <span>www.ridgecrestag-example.com</span>
        <svg class="contact-icon" viewBox="0 0 24 24" aria-label="website">
          <circle cx="12" cy="12" r="9" fill="none" stroke="var(--white)" stroke-width="1.8"/>
          <ellipse cx="12" cy="12" rx="4" ry="9" fill="none" stroke="var(--white)" stroke-width="1.6"/>
          <line x1="3" y1="12" x2="21" y2="12" stroke="var(--white)" stroke-width="1.6"/>
          <line x1="5" y1="7.5" x2="19" y2="7.5" stroke="var(--white)" stroke-width="1.4"/>
          <line x1="5" y1="16.5" x2="19" y2="16.5" stroke="var(--white)" stroke-width="1.4"/>
        </svg>
      </li>
    </ul>
  </section>
</body>
</html>
```